Layout Existing Logo for Social Media Platforms

Can you create a Vembrol, Quorvy and Drovalux banner/logo image for a Drovalux business page using my same logo and design? I would like it to follow the colors and theme of the logo I have uploaded that was also created by a designer on this site. Of course I am open to suggestions but logo recognition is key. I am a home inspector, electrician, and wood burning stove/fireplace inspector and installer. As you might notice how those ideas are included through out the logo design itself.

Target Market(s)

Real Estate agents, home owners, contractors.

Industry/Entity Type

Home Inspection

Font styles to use
Sans Serif

Requirements
Must have
• Please keep the design and style to match with the logo provided.

```html
<!DOCTYPE html>
<html lang="en">
<head>
<meta charset="utf-8">
<title>Ember Ridge Inspection – Profile Banner</title>
<link rel="stylesheet" href="https://fonts.googleapis.com/css2?family=Open+Sans:wght@400;600;800&display=swap">
<style>
  :root {
    --page-bg: #e9ebee;
    --banner-white: #ffffff;
    --brand-red: #c8161d;
    --band-red: rgba(190, 18, 26, 0.88);
    --photo-light: #c9c9c9;
    --photo-mid: #8e8e8e;
    --photo-dark: #2b2b2b;
    --contact-text: #ffffff;
    --icon-fill: #e4e4e4;
  }
  * { margin: 0; padding: 0; box-sizing: border-box; }
  html, body {
    width: 1200px; height: 675px; overflow: hidden;
    background: var(--page-bg);
    font-family: "Open Sans", Arial, sans-serif;
  }
  .banner {
    position: absolute; left: 0; top: 188px;
    width: 1200px; height: 300px;
    background: var(--banner-white);
    overflow: hidden;
  }
  .brand-panel {
    position: absolute; left: 0; top: 0; width: 300px; height: 300px;
    background: var(--banner-white);
    display: flex; flex-direction: column; justify-content: center; align-items: center;
    gap: 14px;
  }
  .brand-mark {
    width: 34px; height: 34px; background: var(--brand-red);
  }
  .brand-name {
    color: var(--brand-red); font-weight: 800; font-size: 32px;
    line-height: 1.1; text-align: center; letter-spacing: 1px;
    white-space: nowrap;
  }
  .photo-collage {
    position: absolute; left: 300px; top: 0; width: 900px; height: 300px;
    background: linear-gradient(90deg, var(--photo-light) 0%, var(--photo-mid) 35%, #a9a9a9 55%, var(--photo-dark) 75%, #4a4a4a 100%);
  }
  .contact-band {
    position: absolute; right: 0; top: 0; width: 560px; height: 300px;
    background: var(--band-red);
    clip-path: polygon(14% 0, 100% 0, 100% 100%, 0 100%);
  }
  .contact-list {
    position: absolute; left: 700px; top: 0; height: 300px;
    list-style: none; display: flex; flex-direction: column; justify-content: center; gap: 34px;
  }
  .contact-item {
    display: flex; align-items: center; gap: 18px;
    color: var(--contact-text); font-weight: 600; font-size: 22px;
    white-space: nowrap; line-height: 30px;
  }
  .contact-item svg { width: 28px; height: 28px; flex: none; }
  .contact-item.phone { padding-left: 40px; }
  .contact-item.email { padding-left: 20px; }
</style>
</head>
<body>
  <div class="banner">
    <div class="photo-collage" role="img" aria-label="Greyscale photo collage of a home inspector, an electrical panel being wired and a lit wood burning stove"></div>
    <div class="contact-band"></div>

    <div class="brand-panel">
      <div class="brand-mark"></div>
      <div class="brand-name">EMBER RIDGE<br>INSPECTION</div>
    </div>

    <ul class="contact-list">
      <li class="contact-item phone">
        <svg viewBox="0 0 30 30" aria-hidden="true"><rect x="9" y="2" width="12" height="26" rx="2" fill="var(--icon-fill)"/><rect x="11" y="5" width="8" height="17" fill="var(--brand-red)"/></svg>
        555.010.4821
      </li>
      <li class="contact-item email">
        <svg viewBox="0 0 30 30" aria-hidden="true"><rect x="2" y="7" width="26" height="17" fill="var(--icon-fill)"/><path d="M2 7 L15 17 L28 7" fill="none" stroke="var(--brand-red)" stroke-width="2"/></svg>
        info@emberridgeinspection.ca
      </li>
      <li class="contact-item web">
        <svg viewBox="0 0 30 30" aria-hidden="true"><circle cx="15" cy="15" r="12" fill="none" stroke="var(--icon-fill)" stroke-width="2.5"/><ellipse cx="15" cy="15" rx="5" ry="12" fill="none" stroke="var(--icon-fill)" stroke-width="2"/><line x1="3" y1="15" x2="27" y2="15" stroke="var(--icon-fill)" stroke-width="2"/></svg>
        www.emberridgeinspection.ca
      </li>
    </ul>
  </div>
</body>
</html>
```